Personal creative Biz Card Design

Need personal yet natural and organic design. The cards I have now are well designed but look too commercial. I want more organic FEELING kind of card. I thought having a headshot would make it more personal... but maybe a sketch effect (or line drawing effect) of face better (?). Maybe in a gray or tungsten color?

Target Market(s)

Well, everyone i give card to will have already seen me face-to-face so that is one thing. Mostly yoga students and people interested in improving their fitness or general health. People looking for wellness, a personal fitness trainer, a yoga teacher

Industry/Entity Type

Health And Wellness

Contact Information for Business Card

I provided examples

Requirements
Must have
• My main logo
• My name

```html
<!DOCTYPE html>
<html lang="en">
<head>
<meta charset="utf-8">
<title>Noel Marsh – Business Card</title>
<link rel="stylesheet" href="https://fonts.googleapis.com/css2?family=Source+Sans+3:wght@400;700&display=swap">
<style>
  :root {
    --backdrop: #b9b9b9;
    --card: #141414;
    --card-edge: #222222;
    --green: #3db843;
    --green-soft: #5fcf55;
    --text-light: #f2f2f2;
    --rule: #3a3a3a;
    --photo-top: #8a8576;
    --photo-bottom: #ece9d8;
  }
  * { box-sizing: border-box; margin: 0; padding: 0; }
  html, body { width: 1200px; height: 900px; overflow: hidden; }
  body {
    background: var(--backdrop);
    font-family: "Source Sans 3", "Helvetica Neue", Arial, sans-serif;
    position: relative;
  }
  .card {
    position: absolute;
    left: 280px;
    width: 640px;
    height: 366px;
    background: radial-gradient(ellipse at 60% 40%, var(--card-edge), var(--card) 70%);
    box-shadow: 0 6px 18px rgba(0,0,0,0.35);
    overflow: hidden;
  }
  .card--services { top: 48px; }
  .card--contact { top: 486px; }

  .brand {
    display: flex;
    align-items: center;
    gap: 12px;
  }
  .brand__dot {
    width: 22px; height: 22px;
    border-radius: 50%;
    background: var(--green);
  }
  .brand__name {
    color: var(--green);
    font-weight: 700;
    font-size: 40px;
    letter-spacing: 1px;
  }

  .card--services .brand {
    position: absolute;
    top: 86px; left: 0; right: 0;
    justify-content: center;
  }
  .services {
    position: absolute;
    top: 170px; left: 0; right: 0;
    list-style: none;
    text-align: center;
    color: var(--green);
    font-size: 20px;
    line-height: 27px;
  }

  .portrait {
    position: absolute;
    left: 0; top: 40px;
    width: 250px; height: 326px;
    background: linear-gradient(180deg, var(--photo-top) 0%, var(--photo-bottom) 45%, var(--photo-bottom) 100%);
    border-radius: 90px 110px 0 0;
  }
  .card--contact .brand {
    position: absolute;
    top: 110px; left: 318px;
  }
  .card--contact .brand__name { font-size: 36px; }
  .divider {
    position: absolute;
    left: 300px; right: 50px; top: 196px;
    border-top: 1px solid var(--rule);
  }
  .contacts {
    position: absolute;
    right: 34px; top: 222px;
    list-style: none;
    color: var(--text-light);
    font-size: 22px;
    line-height: 34px;
    text-align: right;
  }
  .contacts li { display: flex; align-items: center; justify-content: flex-end; gap: 16px; }
  .contacts svg { width: 16px; height: 16px; flex: none; }
</style>
</head>
<body>
  <section class="card card--services">
    <div class="brand">
      <span class="brand__dot"></span>
      <span class="brand__name">NOEL MARSH</span>
    </div>
    <ul class="services">
      <li>Teacher of Yoga | Leader of Yoga Teacher Trainings</li>
      <li>Personal Fitness Trainer | Private &amp; Public classes/Sessions</li>
      <li>Nutrition, Wellness, Meditation</li>
      <li>Healing ceremonies (Puja &amp; Shamanic) | Certified &amp; Insured</li>
    </ul>
  </section>

  <section class="card card--contact">
    <div class="portrait" role="img" aria-label="Headshot of the yoga teacher, smiling, in a cream long-sleeve shirt"></div>
    <div class="brand">
      <span class="brand__dot"></span>
      <span class="brand__name">NOEL MARSH</span>
    </div>
    <div class="divider"></div>
    <ul class="contacts">
      <li>555-014-2287
        <svg viewBox="0 0 16 16" aria-hidden="true"><path fill="var(--green)" d="M3.5 1.5l2.5 3-1.5 1.6c.9 2 2.4 3.5 4.4 4.4L10.5 9l3 2.5-1.2 2.3c-.3.5-.9.7-1.5.5C6.3 13 3 9.7 1.7 5.2c-.2-.6 0-1.2.5-1.5z"/></svg>
      </li>
      <li>noelinwardpaths@example.com
        <svg viewBox="0 0 16 16" aria-hidden="true"><rect x="1" y="3" width="14" height="10" fill="var(--green)"/><path d="M1 3l7 6 7-6" fill="none" stroke="var(--card)" stroke-width="1.4"/></svg>
      </li>
      <li>www.noelmarsh.com
        <svg viewBox="0 0 16 16" aria-hidden="true"><circle cx="8" cy="8" r="7" fill="var(--green)"/><ellipse cx="8" cy="8" rx="3" ry="7" fill="none" stroke="var(--card)" stroke-width="1.1"/><path d="M1 8h14" stroke="var(--card)" stroke-width="1.1"/></svg>
      </li>
    </ul>
  </section>
</body>
</html>
```